Vornel Estates - Chat n’ Cheer Thursday Graphic Invite

We need a graphic design for a corporate reception that we are calling Chat n’ Cheer Thursday. The invite should read:

"QBR invites you to join us at Chat n’ Cheer Thursday

Monday, Jan 22nd
6:30 - 8:30 pm EST

Copper Ladle - Lounge Room

48210 E Pelican Grove Rd
Aventura, FL 33180

Join us for excellent wine and tasty bites at our semi-annual DAW reception. Swing by whenever you can – timing is casual and we'd love to see you there!"

Please feel free to use fun photos from the Copper Ladle gallery: https://www.copperladlegrill.com/photos

Also, please use the QBR logo attached.

Target Market(s)

Corporate professional

Colors
0054AA
0677BA
7BADD7
CADEEF
E8F1F8

Requirements
Must have
• QBR logo, attached verbiage

```html
<!DOCTYPE html>
<html lang="en">
<head>
<meta charset="utf-8">
<title>QBR – Chat n’ Cheer Thursday Invite</title>
<link href="https://fonts.googleapis.com/css2?family=Exo+2:wght@300;600;700&family=Roboto:wght@300;400;500&display=swap" rel="stylesheet">
<style>
  :root {
    --navy: #1f3f8f;
    --blue: #0054aa;
    --mid-blue: #0677ba;
    --sky: #7badd7;
    --ice: #cadeef;
    --mist: #e8f1f8;
    --paper: #fbfbfb;
    --ink-soft: #6b6b6b;
    --ink: #3a3a3a;
    --rule: #c9c9c9;
    --stage: #dfe8ef;
  }
  * { box-sizing: border-box; margin: 0; padding: 0; }
  html, body { width: 1200px; height: 853px; overflow: hidden; background: var(--stage); }
  .invite {
    position: absolute; left: 50px; top: 136px; width: 1100px; height: 580px;
    background: var(--paper); overflow: hidden;
    box-shadow: 0 10px 30px rgba(20, 40, 70, .18);
    font-family: "Roboto", Arial, sans-serif;
  }
  .invite-heading { position: absolute; left: 70px; top: 60px; }
  .invite-lead {
    font-family: "Exo 2", Arial, sans-serif; font-weight: 300;
    font-size: 44px; color: var(--sky); letter-spacing: -.5px; line-height: 1.1;
  }
  .invite-title {
    font-family: "Exo 2", Arial, sans-serif; font-weight: 600;
    font-size: 46px; color: var(--navy); letter-spacing: -.5px; line-height: 1.1;
  }
  .invite-body {
    position: absolute; left: 72px; top: 196px; width: 380px;
    font-size: 17px; font-weight: 300; color: var(--ink-soft); line-height: 1.35;
  }
  .invite-body p + p { margin-top: 16px; }
  .event-details {
    position: absolute; left: 72px; top: 326px; width: 250px;
    border-top: 1px solid var(--rule); border-bottom: 1px solid var(--rule);
    padding: 24px 0 26px;
  }
  .event-when { display: flex; align-items: center; gap: 12px; margin-bottom: 12px; }
  .event-when svg { flex: none; }
  .event-date {
    font-size: 17px; font-weight: 500; color: var(--navy); line-height: 1.25;
  }
  .event-venue { font-size: 17px; font-weight: 400; color: var(--ink); line-height: 1.3; }
  .brand {
    position: absolute; left: 400px; top: 448px;
    display: flex; align-items: center; gap: 14px;
  }
  .brand-square { width: 46px; height: 46px; background: var(--navy); }
  .brand-name {
    font-family: "Exo 2", Arial, sans-serif; font-weight: 600;
    font-size: 52px; color: var(--navy); letter-spacing: 1px;
  }
  .venue-photo { position: absolute; right: 0; top: 0; width: 560px; height: 580px; }
</style>
</head>
<body>
  <section class="invite">
    <svg class="venue-photo" viewBox="0 0 560 580" role="img" aria-label="Photo from the Copper Ladle gallery: cocktails and whiskey glasses at the lounge bar">
      <defs>
        <linearGradient id="photo-tone" x1="0" y1="0" x2="1" y2="1">
          <stop offset="0" stop-color="#d9a24a"/>
          <stop offset=".45" stop-color="#8a5a2c"/>
          <stop offset="1" stop-color="#3f2516"/>
        </linearGradient>
      </defs>
      <polygon points="260,190 560,190 560,580 440,580 200,340" fill="url(#photo-tone)"/>
    </svg>

    <header class="invite-heading">
      <p class="invite-lead">QBR invites you to join us at</p>
      <h1 class="invite-title">Chat n’ Cheer Thursday</h1>
    </header>

    <div class="invite-body">
      <p>Join us for excellent wine and tasty bites at our semi-annual DAW reception.</p>
      <p>Swing by whenever you can – timing is casual and we’d love to see you there!</p>
    </div>

    <div class="event-details">
      <div class="event-when">
        <svg width="30" height="30" viewBox="0 0 30 30" aria-hidden="true">
          <circle cx="15" cy="15" r="13.5" fill="none" stroke="var(--navy)" stroke-width="1.6"/>
          <circle cx="15" cy="15" r="10" fill="none" stroke="var(--navy)" stroke-width=".8"/>
          <path d="M15 8v7l4 3" fill="none" stroke="var(--navy)" stroke-width="1.6" stroke-linecap="round"/>
        </svg>
        <p class="event-date">Monday, Jan 22nd<br>6:30 - 8:30 pm EST</p>
      </div>
      <address class="event-venue" style="font-style:normal">
        Copper Ladle - Lounge Room<br>
        48210 E Pelican Grove Rd<br>
        Aventura, FL 33180
      </address>
    </div>

    <div class="brand">
      <span class="brand-square" aria-hidden="true"></span>
      <span class="brand-name">QBR</span>
    </div>
  </section>
</body>
</html>
```